Shopguidance.net

I've attached two different logo's which I both like and would like to see different designs with each logo. I'm starting a retail consulting business and blog. You can view the start of my project at shopguidance.net to get an idea of what I'm creating.
Looking for a design that says creative, strategic and community.
Updates
Hello Everyone,
Thank you for the amazing design so far.
What I Like
- double sided designs, front and back
- one side should be white or green. Customers cannot write on or make notes on an all black card
- Simple, cool, creative is best
My business card will only have the following
- Instagram
- Facebook
- Email
- Website
My new Tag line is
Plan Well. Guide Well. Grow Well.
My title will be:
Tobin Marlowe
Retail Consultant
Please submit 1 or 2 designs with these specifications.
Thank you,
Tobin
Reason: Looking for a few more designs and have now committed the project and it is no longer refundable. Please read brief and follow specific instructions.
Looking for something simple yet creative. Something that may stand out from most cards.
Thank you,
Tobin
Thank you,
Tobin
Target Market(s)
My main target is retail managers and retail businesses that are focused on leadership and people development.
Industry/Entity Type
Retail
Look and feel
Each slider illustrates characteristics of the customer's brand and the style your logo design should communicate.

```html
<!DOCTYPE html>
<html lang="en">
<head>
<meta charset="utf-8">
<title>Shopguidance.net business card</title>
<link rel="stylesheet" href="https://fonts.googleapis.com/css2?family=Jost:wght@400;500&family=Open+Sans:ital,wght@0,400;0,700;1,400&display=swap">
<style>
  :root {
    --green: #76bf43;
    --green-deep: #2fa84a;
    --charcoal: #343434;
    --charcoal-dark: #262626;
    --white: #ffffff;
    --ink: #2b2b2b;
    --page: #eef2e6;
    --rule: #b9b9b9;
  }
  * { box-sizing: border-box; margin: 0; padding: 0; }
  html, body { width: 1200px; height: 1123px; overflow: hidden; }
  body { background: var(--page); position: relative; font-family: "Open Sans", sans-serif; }

  .card {
    position: absolute; left: 160px; width: 880px; height: 500px; overflow: hidden;
    box-shadow: 0 10px 24px rgba(0,0,0,0.35);
  }
  .card--front { top: 40px; background: repeating-linear-gradient(45deg, var(--charcoal) 0 3px, var(--charcoal-dark) 3px 5px); }
  .card--back { top: 583px; background: var(--white); }

  .tab { position: absolute; background: var(--green); }
  .card--front .tab { right: 0; top: 0; width: 448px; height: 88px; border-bottom-left-radius: 72px; }
  .card--back .tab { right: 0; bottom: 0; width: 450px; height: 120px; border-top-left-radius: 72px; }

  .brand { position: absolute; display: flex; align-items: center; }
  .brand__dot { border-radius: 50%; background: var(--green-deep); flex: none; }
  .brand__name { font-family: "Jost", sans-serif; font-weight: 500; color: var(--white); line-height: 1; }
  .brand__tagline { font-family: "Jost", sans-serif; color: var(--green); letter-spacing: 0.5px; }

  .card--front .brand { left: 120px; top: 165px; }
  .card--front .brand__dot { width: 100px; height: 100px; margin-right: 24px; }
  .card--front .brand__name { font-size: 66px; }
  .card--front .brand__tagline { font-size: 26px; margin-top: 10px; }

  .band { position: absolute; left: 0; top: 0; width: 100%; height: 180px;
    background: repeating-linear-gradient(45deg, var(--charcoal) 0 3px, var(--charcoal-dark) 3px 5px); }
  .band-rule { position: absolute; left: 0; top: 180px; width: 100%; height: 6px;
    background: linear-gradient(90deg, #e0e0e0, var(--rule) 40%, #8c8c8c); }
  .card--back .brand { left: 175px; top: 28px; }
  .card--back .brand__dot { width: 86px; height: 86px; margin-right: 18px; }
  .card--back .brand__name { font-size: 54px; }
  .card--back .brand__tagline { font-size: 20px; margin-top: 8px; }

  .backdrop { position: absolute; left: 0; top: 186px; width: 320px; height: 314px;
    background: radial-gradient(circle at 90% 0%, rgba(118,191,67,0.2), rgba(118,191,67,0.06) 45%, rgba(255,255,255,0) 70%); }

  .person { position: absolute; right: 485px; top: 245px; text-align: right; }
  .person__name { font-size: 36px; font-weight: 700; color: var(--green-deep); line-height: 1.1; }
  .person__title { font-size: 24px; font-style: italic; color: var(--green-deep); }
  .divider { position: absolute; left: 425px; top: 240px; width: 3px; height: 120px; background: var(--green-deep); }

  .contacts { position: absolute; left: 450px; top: 250px; list-style: none; }
  .contacts li { display: flex; align-items: center; font-size: 25px; color: var(--ink); height: 46px; }
  .contacts svg { width: 26px; height: 26px; margin-right: 16px; fill: var(--green-deep); }

  .social { position: absolute; left: 590px; top: 425px; display: flex; gap: 26px; }
  .social__mark { width: 36px; height: 36px; background: var(--white); border-radius: 4px; }
</style>
</head>
<body>
  <section class="card card--front" aria-label="Card front">
    <div class="tab"></div>
    <div class="brand">
      <span class="brand__dot"></span>
      <div>
        <div class="brand__name">Shopguidance</div>
        <div class="brand__tagline">Plan Well. Guide Well. Grow Well</div>
      </div>
    </div>
  </section>

  <section class="card card--back" aria-label="Card back">
    <div class="band"></div>
    <div class="band-rule"></div>
    <div class="brand">
      <span class="brand__dot"></span>
      <div>
        <div class="brand__name">Shopguidance</div>
        <div class="brand__tagline">Plan Well. Guide Well. Grow Well</div>
      </div>
    </div>
    <div class="backdrop" role="img" aria-label="Faint green brand decoration"></div>
    <div class="person">
      <div class="person__name">Tobin Marlowe</div>
      <div class="person__title">Retail Consultant</div>
    </div>
    <div class="divider"></div>
    <ul class="contacts">
      <li><svg viewBox="0 0 24 24" aria-hidden="true"><rect x="2" y="5" width="20" height="14" rx="2"/><path d="M3 6l9 7 9-7" stroke="#fff" stroke-width="2" fill="none"/></svg>tobin@shopguidance.net</li>
      <li><svg viewBox="0 0 24 24" aria-hidden="true"><circle cx="12" cy="7" r="5"/><path d="M2 23c0-6 4.5-9 10-9s10 3 10 9z"/></svg>www.shopguidance.net</li>
    </ul>
    <div class="tab"></div>
    <div class="social">
      <span class="social__mark" role="img" aria-label="Social profile one"></span>
      <span class="social__mark" role="img" aria-label="Social profile two"></span>
      <span class="social__mark" role="img" aria-label="Social profile three"></span>
    </div>
  </section>
</body>
</html>
```